Stationary

We have designed a new logo and business care.
It is now time for stationary.
We are a financial planning firm and are looking for something more formal that show the strength of our firm.
Please include our tag line; Integrity - Vision -Diligence.
I have uploaded a PDF of our current stationary - but - you are under no obligation to design anything like it.
Thx
Marta
Business

```html
<!DOCTYPE html>
<html lang="en">
<head>
<meta charset="utf-8">
<title>Northern Summit Group Stationery</title>
<link rel="stylesheet" href="https://fonts.googleapis.com/css2?family=Quicksand:wght@400;500;700&display=swap">
<style>
  :root {
    --brand-blue: #1578bf;
    --navy: #2b3990;
    --tag-grey: #6d6e71;
    --edge-grey: #a7a9ac;
    --band-grey: #e6e7e8;
    --paper: #ffffff;
  }
  * { margin: 0; padding: 0; box-sizing: border-box; }
  html, body { width: 1200px; height: 777px; overflow: hidden; background: var(--paper); }
  body { position: relative; font-family: "Quicksand", sans-serif; }

  .sheet { position: absolute; background: var(--paper); border: 1px solid var(--edge-grey); overflow: hidden; }

  .letterhead { left: 38px; top: 61px; width: 515px; height: 665px; }
  .envelope-back { left: 474px; top: 249px; width: 573px; height: 272px; }
  .envelope-front { left: 596px; top: 342px; width: 574px; height: 272px; }

  .top-band { position: absolute; left: 0; right: 0; top: 0; }
  .letterhead .top-band { height: 8px; background: var(--brand-blue); }
  .envelope-back .top-band { height: 6px; background: var(--band-grey); }

  .wordmark { position: absolute; color: var(--navy); font-weight: 500; font-size: 24px; white-space: nowrap; line-height: 1; }
  .tagline { position: absolute; color: var(--tag-grey); font-weight: 700; font-size: 10px; letter-spacing: 5.6px; white-space: nowrap; line-height: 1; }

  .mark { position: absolute; display: flex; align-items: center; gap: 5px; color: var(--navy); font-weight: 500; line-height: 1; }
  .mark .dot { width: 12px; height: 12px; border-radius: 50%; background: var(--navy); }

  .letterhead .mark { left: 150px; top: 36px; font-size: 24px; }
  .letterhead .wordmark { left: 232px; top: 30px; }
  .letterhead .tagline { left: 232px; top: 58px; }
  .letterhead .footer { position: absolute; left: 0; right: 0; top: 642px; text-align: center; color: var(--navy); font-size: 8.5px; font-weight: 500; }

  .envelope-back .mark { left: 10px; top: 16px; font-size: 20px; }
  .envelope-back .return-address { position: absolute; left: 12px; top: 46px; color: var(--navy); font-size: 8.4px; font-weight: 500; line-height: 10px; }

  .envelope-front svg.flap { position: absolute; left: 0; top: 0; }
  .envelope-front .wordmark { left: 0; right: 0; top: 24px; text-align: center; }
  .envelope-front .tagline { left: 0; right: 0; top: 52px; text-align: center; }
</style>
</head>
<body>

<section class="sheet letterhead" aria-label="Letterhead">
  <div class="top-band"></div>
  <div class="mark"><span class="dot"></span>NSG</div>
  <div class="wordmark">NorthernSummitGroup</div>
  <div class="tagline">Clarity Foresight Resolve</div>
  <p class="footer">2270 W. Larkspur Ave. • Fairview, Oregon 97024 • P.555.014.2290 • F.555.014.2291 • www.nsgplanning.com</p>
</section>

<section class="sheet envelope-back" aria-label="Envelope, address side">
  <div class="top-band"></div>
  <div class="mark"><span class="dot"></span>NSG</div>
  <p class="return-address">Northern Summit Group<br>2270 W. Larkspur Ave.<br>Fairview, Oregon 97024</p>
</section>

<section class="sheet envelope-front" aria-label="Envelope, flap side">
  <svg class="flap" width="574" height="272" viewBox="0 0 574 272" aria-hidden="true">
    <polyline points="0,0 286,139 574,0" fill="none" stroke="var(--edge-grey)" stroke-width="1.2"/>
  </svg>
  <div class="wordmark">NorthernSummitGroup</div>
  <div class="tagline">Clarity Foresight Resolve</div>
</section>

</body>
</html>
```